Local jobs for students, local vendor post jobs, register users (students) receive notification

I need a simple app design for local shops to post jobs, register users (students) will then receive notifications base on their location (district...)

University students and local shops (flower, coffee, restaurant, etc.)

• Open up app:
• Page 1: Show 2 buttons: View recent jobs and Post a New Jobs
• Login/Registration pages
• Page 2: User registration (Name, Email, Phone and Login with Lumora)
• Page 3: User selection - Students or Local Shops
• Page 3a: If students - fill in the school name, select city, select districts that able to work, maximum 3 selection.
• Page 3b: If local shops - fill in the business name, select the business type (flower, coffee, restaurants, etc.), upload shop image, minimum 1 image maximum 3 images.
• Page 4a: Complete registration - View jobs button if student
• Page 4b: Complete registration - View post job button if vendors
• Signed in pages:
• On click view jobs button:
• Page 5a - Student - List of recent jobs (posted within 48 hours) with premium job display on top, list by most recent, small image of shop, short description, 3 lines of text, click an item to view more.
• Once click on item, show full contents (75 words maximum) with images, and a CALL NOW BUTTON
• On click post jobs button:
• Page 5b - Post job page - input job description in 50 words, select post type (free or premium)
• If premium select, payment type drop-down: show the description of the premium post (3 lines of texts), Credit Card payment inputs.
• Proceed to payment verification:
• Preview Post - Submit button
• DESIGN
• Font - Proxima Nova, Open Sans, Roboto (Unikey friendly, as the app will be in Vietnamese, will provide translation later)
• Style - Flat, Clean
• Color - Bold

```html
<!DOCTYPE html>
<html lang="en">
<head>
<meta charset="utf-8">
<title>Register</title>
<link href="https://fonts.googleapis.com/css2?family=Roboto:wght@400;500&display=swap" rel="stylesheet">
<style>
  :root {
    --page-bg: #e5e5e5;
    --screen-bg: #3e1540;
    --text: #ffffff;
    --muted: #8e7590;
    --line: #b9a8ba;
    --accent: #12ada3;
  }
  * { box-sizing: border-box; margin: 0; padding: 0; }
  html, body {
    width: 1200px; height: 675px; overflow: hidden;
    background: var(--page-bg);
    font-family: "Roboto", Arial, sans-serif;
    color: var(--text);
  }
  .screen {
    position: absolute; left: 422px; top: 21px;
    width: 356px; height: 633px;
    background: var(--screen-bg);
  }
  .screen > * { position: absolute; }
  .title {
    top: 66px; left: 0; width: 100%;
    text-align: center; font-size: 22px; font-weight: 500;
  }
  .subtitle {
    top: 98px; left: 50%; transform: translateX(-50%); width: 270px;
    text-align: center; font-size: 12.5px; line-height: 17px;
  }
  .field {
    left: 38px; width: 273px;
    border-bottom: 1.5px solid var(--line);
    font-size: 16px; color: var(--muted); padding-bottom: 4px;
  }
  .field-name { top: 166px; }
  .field-email { top: 212px; height: 37px; }
  .field-phone { top: 274px; height: 31px; }
  .role-label { top: 332px; left: 38px; font-size: 19px; }
  .chip {
    top: 328px; height: 29px;
    border: 1.5px solid var(--accent); border-radius: 15px;
    font-size: 12.5px; font-weight: 500;
    display: flex; align-items: center; justify-content: center;
  }
  .chip-student { left: 127px; width: 89px; }
  .chip-shop { left: 222px; width: 89px; }
  .btn-register {
    top: 393px; left: 114px; width: 128px; height: 45px;
    background: var(--accent); border-radius: 23px;
    font-size: 16.5px; font-weight: 500;
    display: flex; align-items: center; justify-content: center;
  }
  .btn-social {
    top: 463px; left: 62px; width: 238px; height: 46px;
    border: 1.5px solid var(--text); border-radius: 23px;
    font-size: 17px; font-weight: 500;
    display: flex; align-items: center; justify-content: center; gap: 8px;
  }
  .btn-social .mark { width: 17px; height: 17px; background: var(--text); border-radius: 2px; }
  .footer {
    top: 572px; left: 0; width: 100%;
    text-align: center; font-size: 15.5px; font-weight: 500;
  }
  .footer a { color: var(--accent); text-decoration: underline; }
</style>
</head>
<body>
  <main class="screen">
    <h1 class="title">Register</h1>
    <p class="subtitle">Lorem ipsum dolor sit amet, consectetur adipiscing elit,</p>
    <div class="field field-name">Name</div>
    <div class="field field-email">Email</div>
    <div class="field field-phone">Phone Number</div>
    <span class="role-label">I am a</span>
    <div class="chip chip-student">Student</div>
    <div class="chip chip-shop">Local Shop</div>
    <div class="btn-register">Register</div>
    <div class="btn-social"><span class="mark"></span>Login using Lumora</div>
    <p class="footer">Existing User? <a href="#login">Login Here</a></p>
  </main>
</body>
</html>
```